Billboard Design for Equipment Rental Business

We need a billboard design for our equipment rental business called Brindlewood Equipment Company. We are based in Georgia. We rent construction tools, equipment, and dumpsters. We currently have a design but feel like we could get something better. Our phone number is 912-730-2591 and our website is www.brindlewoodequipment-example.com

```html
<!DOCTYPE html>
<html lang="en">
<head>
<meta charset="utf-8">
<title>Brindlewood Equipment Company – Billboard</title>
<link rel="stylesheet" href="https://fonts.googleapis.com/css2?family=Barlow+Condensed:wght@700&family=Krona+One&family=Montserrat:wght@500&display=swap">
<style>
  :root {
    --backdrop: #d3d3d3;
    --brand-yellow: #f9bc15;
    --ink: #0b0d0c;
    --paper: #ffffff;
  }
  * { box-sizing: border-box; margin: 0; padding: 0; }
  html, body {
    width: 910px;
    height: 1200px;
    overflow: hidden;
    background: var(--backdrop);
  }
  .canvas {
    position: relative;
    width: 910px;
    height: 1200px;
  }
  .billboard {
    position: absolute;
    left: 30px;
    top: 388px;
    width: 850px;
    height: 424px;
    background: var(--paper);
    box-shadow: 2px 3px 6px rgba(0, 0, 0, 0.35);
    overflow: hidden;
  }
  .billboard__upper {
    position: absolute;
    left: 0;
    top: 0;
    width: 100%;
    height: 290px;
    background: var(--brand-yellow);
  }
  .brand-mark {
    position: absolute;
    left: 150px;
    top: 118px;
    width: 64px;
    height: 64px;
    background: var(--ink);
  }
  .brand-name {
    position: absolute;
    left: 250px;
    top: 78px;
    width: 520px;
    font-family: "Barlow Condensed", "Arial Narrow", sans-serif;
    font-weight: 700;
    color: var(--ink);
    text-transform: uppercase;
    line-height: 1;
  }
  .brand-name__primary {
    display: block;
    font-size: 92px;
    letter-spacing: 2px;
  }
  .brand-name__secondary {
    display: block;
    margin-top: 6px;
    font-size: 34px;
    letter-spacing: 3.2px;
  }
  .web-pill {
    position: absolute;
    left: 90px;
    top: 251px;
    width: 680px;
    height: 60px;
    background: var(--ink);
    border-radius: 0 26px 0 26px;
    display: flex;
    align-items: center;
    justify-content: center;
    font-family: "Montserrat", Arial, sans-serif;
    font-weight: 500;
    font-size: 26px;
    color: var(--brand-yellow);
    white-space: nowrap;
  }
  .phone {
    position: absolute;
    left: 0;
    top: 336px;
    width: 100%;
    text-align: center;
    font-family: "Krona One", "Arial Black", sans-serif;
    font-size: 58px;
    line-height: 1;
    color: var(--brand-yellow);
    white-space: nowrap;
  }
</style>
</head>
<body>
  <main class="canvas">
    <section class="billboard" aria-label="Brindlewood Equipment Company billboard">
      <div class="billboard__upper">
        <div class="brand-mark" aria-hidden="true"></div>
        <h1 class="brand-name">
          <span class="brand-name__primary">Brindlewood</span>
          <span class="brand-name__secondary">Equipment Company</span>
        </h1>
      </div>
      <p class="web-pill">www.brindlewoodequipment-example.com</p>
      <p class="phone">912-730-2591</p>
    </section>
  </main>
</body>
</html>
```